Einladungskarten-Design für Ehepaar
Zielgruppe
Wir sind ein Ehepaar und feiern 2 Geburtstage und eine Hochzeit in einem grossen Fest. Unsere Zielgruppe sind unsere Freunde.
Aufgabenstellung
Doppelkarte A5 quer, nur Frontseite designed; Briefing siehe Worddok

```html
<!DOCTYPE html>
<html lang="de">
<head>
<meta charset="utf-8">
<title>Einladung – 2 Geburtstage und 1 Hochzeit</title>
<link rel="stylesheet" href="https://fonts.googleapis.com/css2?family=Questrial&family=Roboto:wght@400&display=swap">
<style>
  :root {
    --page: #ffffff;
    --ink: #111111;
    --wine: #9b1d2c;
    --cloud: #dedbe0;
    --navy: #252a55;
    --lavender: #7b7bb5;
    --maroon: #5c2428;
    --rust: #b4714c;
    --amber: #eba518;
    --white: #ffffff;
  }
  html, body {
    margin: 0;
    padding: 0;
    width: 849px;
    height: 1200px;
    overflow: hidden;
    background: var(--page);
  }
  .sheet {
    position: relative;
    width: 849px;
    height: 1200px;
  }
  .invitation-card {
    position: absolute;
    left: 81px;
    top: 139px;
    width: 641px;
    height: 451px;
    box-shadow: 9px 9px 6px rgba(0,0,0,0.55);
  }
  .invitation-card svg {
    display: block;
    width: 641px;
    height: 451px;
  }
  .card-type {
    font-family: "Questrial", sans-serif;
  }
  .caption {
    position: absolute;
    left: 109px;
    top: 637px;
    margin: 0;
    font-family: "Roboto", sans-serif;
    font-size: 15.5px;
    color: var(--ink);
  }
</style>
</head>
<body>
<main class="sheet">
  <section class="invitation-card">
    <svg viewBox="0 0 641 451" xmlns="http://www.w3.org/2000/svg">
      <defs>
        <linearGradient id="photoTone" x1="0" y1="0" x2="1" y2="1">
          <stop offset="0" stop-color="#1d2a14"/>
          <stop offset="0.3" stop-color="#6d8a3a"/>
          <stop offset="0.5" stop-color="#d9ded8"/>
          <stop offset="0.75" stop-color="#b8c4bc"/>
          <stop offset="1" stop-color="#5f8e94"/>
        </linearGradient>
        <linearGradient id="weddingTone" x1="0" y1="1" x2="1" y2="0">
          <stop offset="0" stop-color="var(--navy)"/>
          <stop offset="1" stop-color="var(--lavender)"/>
        </linearGradient>
        <linearGradient id="birthdayTone" x1="0" y1="0" x2="0" y2="1">
          <stop offset="0" stop-color="var(--maroon)"/>
          <stop offset="1" stop-color="var(--rust)"/>
        </linearGradient>
      </defs>

      <rect class="photo-area" role="img" aria-label="Foto: Brautkleid im Garten, zwei Sektgläser und Flasche auf einer türkisen Holzbank" x="0" y="0" width="641" height="451" fill="url(#photoTone)"/>

      <circle class="bubble-wedding" cx="240" cy="60" r="108" fill="url(#weddingTone)" opacity="0.95"/>
      <circle class="bubble-birthday" cx="150" cy="221" r="79" fill="url(#birthdayTone)" opacity="0.93"/>
      <circle class="bubble-invite" cx="117" cy="403" r="120" fill="var(--amber)" opacity="0.95"/>
      <circle class="bubble-date" cx="71" cy="77" r="77" fill="var(--cloud)" opacity="0.97"/>

      <g class="plus-sign" stroke="var(--white)" stroke-width="2">
        <line x1="128" y1="129" x2="160" y2="129"/>
        <line x1="144" y1="113" x2="144" y2="145"/>
      </g>

      <g class="card-type date-block" fill="var(--wine)" text-anchor="middle">
        <text x="75" y="35" font-size="15" textLength="107" lengthAdjust="spacingAndGlyphs">Jonas&amp; Helena</text>
        <text x="75" y="56" font-size="27" textLength="68" lengthAdjust="spacingAndGlyphs">feiern</text>
        <text x="75" y="77" font-size="15">am</text>
        <text x="74" y="120" font-size="56" textLength="107" lengthAdjust="spacingAndGlyphs">6.10.</text>
      </g>

      <g class="card-type wedding-block" fill="var(--white)" text-anchor="middle">
        <text x="240" y="85" font-size="77" textLength="163" lengthAdjust="spacingAndGlyphs">2018</text>
        <text x="240" y="118" font-size="28" textLength="106" lengthAdjust="spacingAndGlyphs">Hochzeit</text>
      </g>

      <g class="card-type birthday-block" fill="var(--white)" text-anchor="middle">
        <text x="151" y="213" font-size="54" textLength="97" lengthAdjust="spacingAndGlyphs">2<tspan font-size="13">x</tspan>60</text>
        <text x="151" y="251" font-size="28" textLength="138" lengthAdjust="spacingAndGlyphs">Geburtstag</text>
      </g>

      <g class="card-type invite-block">
        <text x="29" y="364" font-size="35" fill="var(--ink)" stroke="var(--ink)" stroke-width="0.8" textLength="181" lengthAdjust="spacingAndGlyphs">EINLADUNG</text>
        <text x="29" y="390" font-size="22" fill="var(--white)" stroke="var(--white)" stroke-width="0.4" textLength="141" lengthAdjust="spacingAndGlyphs">2 Geburtstage</text>
        <text x="29" y="416" font-size="22" fill="var(--white)" textLength="144" lengthAdjust="spacingAndGlyphs">und 1 Hochzeit</text>
      </g>
    </svg>
  </section>

  <p class="caption">Klappkarte Din A 5 auf Wunsch nur Vorne gestaltet.</p>
</main>
</body>
</html>
```